Aircraft maintenance buisness card

I am an aircraft mechanic looking for a personal buisness card . I would like my name and a title of Aircraft Maintenance Manager . I would like a suttle picture of an aircraft and helicopter .

elegant and professional wtih my contact .

My name should be on the car and Aircraft Maintenance Manager under with my contact infor below .

i have attached some pictures but i am open to other pics and ideas . I would like a airliner or private jet and a helicopter in the picture . The Images should be suttle and not the main idea . I also uploaded a picture of a jet engine which is cool . Be creative and i will work with you to finalize something .
Updates

Project Deadline Extended
Reason: Looking for more variations . Very good so far but looiking for a bit more styles and i uploaded my logo that i purchased . Please use my logo and be creative with it . I like some variations of black card with maybe some pictures that i uploaded but i am open to ideas . Be creative and i will work with you .

Project Deadline Extended
Reason: Looking for more designs and variations . Not yet satisfied with the designs i have gotten .

Industry/Entity Type

Aviation

Contact Information for Business Card

Aircraft Maintenance Manager

Font styles to use
Serif

Colors

Designer to choose colors to be used in the design.

Requirements
Must have
• An aviation related Logo if possible incorporated in the card possibly
• My name
• Tiberio Malvade Furtunato
• 482 Pellow St.
• Kearny , NJ
• 08519
• Email: Lwskyfixtech@mailvora.com
Nice to have
• Suttle Backround of a Private Jet or Airliner and a Helicopter .

```html
<!DOCTYPE html>
<html lang="en">
<head>
<meta charset="utf-8">
<title>Aircraft Maintenance Manager – Business Card</title>
<link rel="stylesheet" href="https://fonts.googleapis.com/css2?family=Cinzel:wght@400;500;600&display=swap">
<style>
  :root {
    --page-bg: #1a1a1b;
    --card-dark-1: #16181b;
    --card-dark-2: #2b2e32;
    --accent-blue: #4a78c8;
    --text-light: #d9dbde;
    --text-soft: #b9bcc1;
    --rock-1: #8d8a85;
    --rock-2: #a9a49c;
    --rock-3: #6f6c66;
    --sky-mist: #3a4048;
  }
  * { box-sizing: border-box; margin: 0; padding: 0; }
  html, body {
    width: 1200px; height: 1000px; overflow: hidden;
    background: var(--page-bg);
    font-family: "Cinzel", "Times New Roman", serif;
  }
  .stage {
    position: relative; width: 1200px; height: 1000px;
  }
  .card {
    position: absolute; left: 220px; width: 760px; height: 434px;
    overflow: hidden; border-radius: 4px;
    box-shadow: 0 14px 34px rgba(0,0,0,0.55);
  }
  .card-front { top: 48px; }
  .card-back {
    top: 518px;
    background: linear-gradient(160deg, var(--card-dark-2) 0%, var(--card-dark-1) 70%);
  }
  .front-photo {
    position: absolute; inset: 0;
    background:
      radial-gradient(ellipse at 45% 60%, rgba(40,70,160,0.55) 0 12%, transparent 30%),
      linear-gradient(135deg, var(--rock-3) 0%, var(--rock-2) 40%, var(--rock-1) 70%, #5d6a52 100%);
  }
  .back-photo {
    position: absolute; left: 330px; top: 90px; width: 420px; height: 300px;
    background: radial-gradient(ellipse at 55% 45%, rgba(200,210,225,0.22) 0%, rgba(70,80,95,0.2) 40%, transparent 70%);
  }
  .identity { position: absolute; left: 60px; top: 128px; }
  .name {
    color: var(--accent-blue); font-size: 34px; font-weight: 500;
    letter-spacing: 1px; text-transform: uppercase; white-space: nowrap;
  }
  .title {
    color: var(--text-light); font-size: 17px; letter-spacing: 0.5px;
    margin-top: 4px;
  }
  .accent-bar {
    position: absolute; left: 60px; top: 226px;
    width: 72px; height: 4px; background: var(--accent-blue);
  }
  .contact-list { position: absolute; left: 60px; top: 254px; list-style: none; }
  .contact-list li {
    color: var(--text-light); font-size: 17px; letter-spacing: 0.5px;
    line-height: 36px; text-transform: uppercase;
  }
  .label { color: var(--accent-blue); margin-right: 8px; }
  .site-highlight { color: var(--accent-blue); }
  .address { position: absolute; left: 60px; top: 362px; }
  .address-label {
    color: var(--accent-blue); font-size: 16px; letter-spacing: 0.5px;
  }
  .address-line {
    color: var(--text-light); font-size: 17px; letter-spacing: 0.5px;
  }
</style>
</head>
<body>
<main class="stage">
  <section class="card card-front">
    <div class="front-photo" role="img" aria-label="Photo of a blue and white helicopter flying past a grey granite cliff"></div>
  </section>

  <section class="card card-back">
    <div class="back-photo" role="img" aria-label="Faint photo of an airliner in flight seen from the front"></div>
    <div class="identity">
      <h1 class="name">Tiberio Malvade Furtunato</h1>
      <p class="title">Aircraft Maintenance Manager</p>
    </div>
    <div class="accent-bar"></div>
    <ul class="contact-list">
      <li><span class="label">P:</span>000 111 222 333</li>
      <li><span class="label">E:</span>Lwskyfixtech@mailvora.com</li>
      <li><span class="label">W:</span>www.<span class="site-highlight">ursitename</span>.com</li>
    </ul>
    <div class="address">
      <p class="address-label">Address:</p>
      <p class="address-line">482 Pellow St. Kearny , NJ 08519</p>
    </div>
  </section>
</main>
</body>
</html>
```